Irrigation Business needs their business cards modernised and revamped

I would like to keep my current logo, colours and revamp the format of the card.

I would like the card to be clean yet important.

Im not sure if you include texture but i would like the named logo to be indented into the card etc.

show me something alive and free something thats clinical to the point yet has a feel of achievement. i would like people to go nice card.

Target Market(s)

high end clients, corporate, sports field manger, the guys that make the decisions

Industry/Entity Type

Business

Contact Information for Business Card

nformation to be included

Dorian Hesk (Director)
0487253916
dorian@tfcraft.biz
www.taddsfieldcrafts.com

instagram logo
google logo
facebook logo

Colors

Designer to choose colors to be used in the design.

Requirements
Nice to have
• indentations a really nice feel to the card good texture

```html
<!DOCTYPE html>
<html lang="en">
<head>
<meta charset="utf-8">
<title>Tadd's Field Crafts – Business Card</title>
<link rel="stylesheet" href="https://fonts.googleapis.com/css2?family=Lato:wght@400;700;900&display=swap">
<style>
  :root {
    --backdrop: #111111;
    --card: #faf8f2;
    --blue: #2f67ab;
    --sky: #33a5d8;
    --green: #27a14f;
    --white: #ffffff;
    --pattern: #ecebe6;
  }
  * { box-sizing: border-box; margin: 0; padding: 0; }
  html, body {
    width: 1200px; height: 1000px; overflow: hidden;
    background: var(--backdrop);
    font-family: "Lato", sans-serif;
  }
  .stage { position: relative; width: 1200px; height: 1000px; }

  .card {
    position: absolute; top: 355px;
    width: 500px; height: 290px;
    border-radius: 22px; overflow: hidden;
    background: var(--card);
  }
  .card--front { left: 75px; }
  .card--back { left: 625px; }

  /* front */
  .front-bands { position: absolute; left: 0; top: 0; }
  .front-name {
    position: absolute; left: 250px; top: 58px;
    color: var(--sky); font-size: 17px; font-weight: 700;
    letter-spacing: 0.2px;
  }
  .front-name .role { font-weight: 400; }
  .contact-list { position: absolute; left: 195px; top: 100px; list-style: none; }
  .contact-item {
    display: flex; align-items: center; height: 46px;
    color: var(--white); font-size: 15px;
  }
  .contact-icon {
    width: 20px; height: 20px; border-radius: 50%;
    background: rgba(255,255,255,0.85);
    display: flex; align-items: center; justify-content: center;
    margin-right: 10px; flex: none;
  }

  /* back */
  .back-pattern {
    position: absolute; inset: 0;
    background: radial-gradient(circle at 50% 50%, var(--card) 0 28%, var(--pattern) 80%);
  }
  .brand {
    position: absolute; left: 0; right: 0; top: 78px;
    display: flex; flex-direction: column; align-items: center;
  }
  .brand-mark {
    width: 56px; height: 56px; border-radius: 50%;
    background: var(--sky);
  }
  .brand-name {
    margin-top: 10px;
    color: var(--blue); font-size: 26px; font-weight: 900;
    letter-spacing: 0.5px;
  }
  .social-list { display: flex; gap: 12px; margin-top: 16px; list-style: none; }
  .social-dot {
    width: 30px; height: 30px; border-radius: 50%;
    background: var(--sky);
  }
</style>
</head>
<body>
<main class="stage">

  <section class="card card--front" aria-label="Business card front">
    <svg class="front-bands" width="500" height="290" viewBox="0 0 500 290" aria-hidden="true">
      <rect x="0" y="100" width="500" height="150" fill="var(--blue)"/>
      <rect x="0" y="141" width="500" height="5" fill="var(--white)"/>
      <rect x="0" y="187" width="500" height="5" fill="var(--white)"/>
      <rect x="0" y="233" width="500" height="5" fill="var(--white)"/>
      <rect x="0" y="256" width="500" height="34" fill="var(--green)"/>
      <circle cx="110" cy="160" r="76" fill="var(--blue)"/>
      <circle cx="110" cy="160" r="72" fill="none" stroke="var(--white)" stroke-width="4"/>
      <circle cx="110" cy="160" r="62" fill="var(--sky)"/>
    </svg>

    <p class="front-name">DORIAN HESK <span class="role">| Director</span></p>

    <ul class="contact-list">
      <li class="contact-item">
        <span class="contact-icon">
          <svg width="10" height="12" viewBox="0 0 10 12"><rect x="1.5" y="0.5" width="7" height="11" rx="1.5" fill="var(--blue)"/></svg>
        </span>0487 253 916
      </li>
      <li class="contact-item">
        <span class="contact-icon">
          <svg width="12" height="9" viewBox="0 0 12 9"><rect x="0.5" y="0.5" width="11" height="8" fill="var(--blue)"/><path d="M0.5 0.5 L6 5 L11.5 0.5" stroke="var(--white)" fill="none"/></svg>
        </span>dorian@tfcraft.biz
      </li>
      <li class="contact-item">
        <span class="contact-icon">
          <svg width="12" height="12" viewBox="0 0 12 12" fill="none" stroke="var(--blue)" stroke-width="1.2"><circle cx="6" cy="6" r="5"/><ellipse cx="6" cy="6" rx="2.2" ry="5"/><path d="M1 6 H11"/></svg>
        </span>www.taddsfieldcrafts.com
      </li>
    </ul>
  </section>

  <section class="card card--back" aria-label="Business card back">
    <div class="back-pattern" role="img" aria-label="Faint repeating brand pattern across the card"></div>
    <div class="brand">
      <span class="brand-mark" aria-hidden="true"></span>
      <p class="brand-name">TADD'S FIELD CRAFTS</p>
      <ul class="social-list" aria-label="Social media">
        <li class="social-dot"></li>
        <li class="social-dot"></li>
        <li class="social-dot"></li>
      </ul>
    </div>
  </section>

</main>
</body>
</html>
```